Industrial automation company needs new business cards

We need a new business card designed. We have an existing logo that is very simple and are happy to consider changes to it. We have been in business for more than 10 years and our logo has some brand recognition.
We are a company of engineers and build systems for industrial automation, substation automation, power and energy monitoring and production data vertical integration. Our main clients are food manufacturers, data centers and government establishments.
Our current business cards have our name, qualifications, job title, telephone, email and web address details. We don't need our physical address on our business cards. I've attached our current logo

Industry/Entity Type

Business

Logo Text

vardo

Font styles to use
Sans Serif

Colors
6b449b

Requirements
Must have
• - double sided business cards
• - name (eg Mara Quill)
• - qualifications (BE Elec MAGSO)
• - job title (eg Senior Engineer)
• - telephone (eg 0472 518 396)
• - email (eg mara.quill@vardo.com.au)
• - web address (eg vardo.com.au)
Nice to have
• include our target markets on the back side of the card
• - industrial automation
• - substation automation
• - power and energy monitoring
• - production data vertical integration

```html
<!DOCTYPE html>
<html lang="en">
<head>
<meta charset="utf-8">
<title>vardo business cards</title>
<link href="https://fonts.googleapis.com/css2?family=Source+Sans+3:wght@400;600&display=swap" rel="stylesheet">
<style>
  :root{
    --backdrop:#3b332e;
    --card:#0c0b0c;
    --purple:#6b449b;
    --purple-light:#7d55b3;
    --grey:#8a8a8a;
    --silver:#c9c9c9;
    --text:#e8e8e8;
    --rule:#2a2730;
  }
  *{box-sizing:border-box;margin:0;padding:0}
  html,body{width:1200px;height:900px;overflow:hidden}
  body{background:var(--backdrop);font-family:"Source Sans 3",Arial,sans-serif;position:relative}
  .card{position:absolute;width:520px;height:300px;background:var(--card);box-shadow:0 10px 30px rgba(0,0,0,.45)}
  .card--front{left:50px;top:440px}
  .card--back{left:630px;top:160px}

  .brand{position:absolute;display:flex;align-items:center;gap:14px}
  .brand__square{width:44px;height:44px;background:var(--purple)}
  .brand__name{font-size:58px;font-weight:400;line-height:1;letter-spacing:-1px}
  .card--front .brand{left:40px;top:150px}
  .card--front .brand__name{color:var(--grey)}
  .card--back .brand{left:50px;top:120px}
  .card--back .brand__name{color:var(--silver)}

  .divider{position:absolute;top:40px;width:1px;height:150px;background:var(--rule)}
  .card--front .divider{left:280px}
  .card--back .divider{left:240px;top:30px}

  .person{position:absolute;left:305px;top:42px}
  .person__name{color:var(--purple-light);font-weight:600;font-size:19px;letter-spacing:.5px;text-transform:uppercase}
  .person__quals{color:var(--purple-light);font-size:14px;margin-top:2px}
  .person__role{color:var(--text);font-size:15px;margin-top:1px}

  .contact{position:absolute;left:305px;top:130px;list-style:none}
  .contact li{display:flex;align-items:center;gap:9px;color:var(--text);font-size:15px;line-height:20px}
  .contact svg{width:13px;height:13px;flex:none}

  .markets{position:absolute;left:262px;top:40px;list-style:none}
  .markets li{display:flex;align-items:center;gap:10px;color:var(--text);font-size:15px;line-height:29px}
  .markets li::before{content:"";width:7px;height:7px;border-radius:50%;background:var(--text)}
</style>
</head>
<body>
  <section class="card card--front" aria-label="Card front">
    <div class="brand">
      <span class="brand__square"></span>
      <span class="brand__name">vardo</span>
    </div>
    <span class="divider"></span>
    <div class="person">
      <p class="person__name">Mara Quill</p>
      <p class="person__quals">BE Elec MAGSO</p>
      <p class="person__role">Senior Engineer</p>
    </div>
    <ul class="contact">
      <li>
        <svg viewBox="0 0 14 14"><circle cx="7" cy="7" r="7" fill="#6b449b"/><path d="M4 4.5c0 3 2.5 5.5 5.5 5.5l.8-1.3-1.5-.8-.7.6c-1-.4-1.8-1.2-2.2-2.2l.6-.7-.8-1.5z" fill="#0c0b0c"/></svg>
        0472 518 396
      </li>
      <li>
        <svg viewBox="0 0 14 14"><circle cx="7" cy="7" r="7" fill="#6b449b"/><rect x="3.5" y="4.5" width="7" height="5" fill="#0c0b0c"/><path d="M3.5 4.5 7 7.5l3.5-3" stroke="#6b449b" stroke-width=".8" fill="none"/></svg>
        info@vardo.com.au
      </li>
      <li>
        <svg viewBox="0 0 14 14"><circle cx="7" cy="7" r="7" fill="#6b449b"/><circle cx="7" cy="7" r="3.3" fill="none" stroke="#0c0b0c" stroke-width="1"/><path d="M3.7 7h6.6M7 3.7v6.6" stroke="#0c0b0c" stroke-width=".8"/></svg>
        www.vardo.com.au
      </li>
    </ul>
  </section>

  <section class="card card--back" aria-label="Card back">
    <div class="brand">
      <span class="brand__name">vardo</span>
    </div>
    <span class="divider"></span>
    <ul class="markets">
      <li>Industrial Automation</li>
      <li>substation Automation</li>
      <li>Power &amp; Energy Monitoring</li>
      <li>Production Data Vertical Integration</li>
    </ul>
  </section>
</body>
</html>
```